Homepage for the brisk-trail Web Application

At the end of this text, you will find a link to a website that is under construction for a webApp that I intend to launch soon. The contest goal is for you to make redesign the homepage in a nice, fresh, modern Style. Only design, no coding necessary. It needs to have a responsive version for small screens like smart phones. Attached is the text for it, and some images that you may use. You are welcome to find or create additional supporting images. You can use PixVaultimages.com or similar service to find new images as long as I can purchase the non-exclusive use rights for the images at similar prices. The contest is just for the home page. However, the winner, if I like the work and we can agree on a fair price, could be contracted on a one-on-one basis to do the rest of the site. You are welcome to suggest minor changes like font sizes and minor variations on the Header banner, but that banner is consistent with the user interface of the application therefore should not change too much. The information should flow somewhat continually without much use of side bars or things like that.
https://www.brisk-trail-example.com
Sincerely,
Marco R. Delgado

```html
<!DOCTYPE html>
<html lang="en">
<head>
<meta charset="utf-8">
<title>Brisk-Trail — Find that document or item instantly</title>
<link rel="stylesheet" href="https://fonts.googleapis.com/css2?family=Noto+Sans:wght@400;500;600;700&family=Roboto:wght@300;400;500;700&display=swap">
<style>
  :root {
    --orange: #e35d3a;
    --ink: #333638;
    --muted: #55595d;
    --hero-bg: #eaecf0;
    --band-bg: #eaecf1;
    --black: #000000;
    --white: #ffffff;
    --footer-bg: #e2e3e5;
    --btn-dark: #333333;
  }
  * { margin: 0; padding: 0; box-sizing: border-box; }
  html, body { width: 1200px; height: 3951px; overflow: hidden; }
  body { font-family: "Noto Sans", Arial, sans-serif; color: var(--ink); background: var(--white); position: relative; }
  section, header, footer { position: relative; width: 1200px; }
  .abs { position: absolute; }

  /* Hero */
  .hero { height: 675px; background: var(--hero-bg); }
  .hero-side { left: 0; top: 0; width: 375px; height: 675px; background: var(--black); }
  .brand { left: 86px; top: 30px; display: flex; align-items: center; gap: 10px; }
  .brand-dot { width: 42px; height: 42px; border-radius: 50%; background: var(--white); }
  .brand-name { font-size: 34px; font-weight: 400; color: var(--orange); letter-spacing: 0.3px; }
  .nav { left: 430px; top: 42px; display: flex; gap: 22px; font-size: 14px; color: #6b6f73; }
  .nav a { color: inherit; text-decoration: none; padding-bottom: 6px; }
  .nav a.active { color: var(--ink); border-bottom: 2px solid var(--ink); }
  .btn-login { left: 1001px; top: 32px; width: 126px; height: 40px; background: var(--orange); color: var(--white); font-size: 14px; font-weight: 600; display: flex; align-items: center; justify-content: center; }
  .hero-art { left: 88px; top: 145px; width: 475px; height: 485px; border-radius: 18px; background: linear-gradient(150deg, #5fd6dd 0%, #2fb3bc 60%, #e7713f 100%); }
  .hero-title { left: 609px; top: 162px; width: 560px; font-size: 49px; font-weight: 600; line-height: 59px; color: var(--ink); white-space: nowrap; }
  .hero-text { left: 609px; top: 302px; width: 495px; font-size: 14px; line-height: 19.5px; color: var(--muted); }
  .hero-lead { left: 609px; top: 436px; width: 470px; font-size: 18.5px; line-height: 24px; font-weight: 500; color: var(--orange); }
  .btn-contact { left: 609px; top: 528px; width: 182px; height: 42px; background: var(--orange); color: var(--white); font-size: 14px; font-weight: 600; display: flex; align-items: center; justify-content: center; }

  /* Why use */
  .why-use { height: 679px; background: var(--white); }
  .section-heading { font-size: 27px; font-weight: 500; line-height: 35px; color: var(--ink); }
  .why-use .section-heading { left: 86px; top: 105px; width: 470px; }
  .kicker { left: 86px; top: 200px; font-size: 17px; font-weight: 500; color: var(--orange); letter-spacing: 0.3px; }
  .why-copy { left: 86px; top: 249px; width: 495px; font-size: 13.8px; line-height: 19.5px; color: var(--muted); }
  .why-copy p + p { margin-top: 16px; }
  .why-art { left: 637px; top: 50px; width: 468px; height: 567px; border-radius: 26px; background: linear-gradient(135deg, #f0774d 0%, #f0774d 30%, #bff1f4 55%, #3ec1c9 100%); }

  /* Non-document objects */
  .objects { height: 826px; background: var(--band-bg); }
  .center-title { left: 0; width: 1200px; text-align: center; font-size: 28px; font-weight: 600; color: var(--ink); }
  .objects .center-title { top: 72px; }
  .objects-sub { left: 0; width: 1200px; top: 118px; text-align: center; font-size: 15.5px; color: var(--muted); }
  .object-item { left: 84px; width: 1025px; display: flex; gap: 40px; }
  .object-item svg { width: 58px; height: 52px; flex: none; margin-top: 6px; }
  .object-item h3 { font-size: 22px; font-weight: 500; color: var(--ink); margin-bottom: 12px; line-height: 28px; }
  .object-item p { font-size: 13.8px; line-height: 23px; color: var(--muted); }
  .down-btn { left: 574px; top: 703px; width: 52px; height: 52px; border-radius: 50%; background: var(--orange); display: flex; align-items: center; justify-content: center; }

  /* Why Brisk-Trail */
  .reasons { height: 528px; background: var(--white); }
  .reasons .center-title { top: 71px; }
  .reason { left: 106px; width: 960px; display: flex; gap: 18px; font-size: 22.5px; font-weight: 600; line-height: 30px; color: var(--ink); }
  .reason svg { width: 28px; height: 26px; flex: none; margin-top: 2px; }

  /* Testimonials */
  .testimonials { height: 512px; background: var(--black); font-family: "Roboto", Arial, sans-serif; }
  .t-title { left: 0; width: 1180px; top: 66px; text-align: center; font-size: 31px; font-weight: 500; color: var(--white); }
  .t-sub { left: 0; width: 1180px; top: 114px; text-align: center; font-size: 17px; font-weight: 300; color: #8d8f91; }
  .t-quote { left: 290px; width: 600px; top: 180px; text-align: center; font-size: 25px; font-weight: 300; line-height: 39.5px; color: #9a9c9e; white-space: nowrap; }
  .t-arrow { top: 240px; width: 58px; height: 26px; }
  .t-name { left: 0; width: 1200px; top: 384px; text-align: center; font-size: 18px; font-weight: 500; color: var(--white); }
  .t-company { left: 0; width: 1200px; top: 412px; text-align: center; font-size: 10.5px; color: #6d6f71; }
  .t-role { left: 0; width: 1200px; top: 429px; text-align: center; font-size: 10.5px; color: var(--orange); }

  /* Blog */
  .blog { height: 648px; background: var(--white); }
  .blog .center-title { top: 72px; font-weight: 500; }
  .blog-rule { left: 567px; top: 121px; width: 66px; height: 2px; background: #c9cbcd; }
  .post { top: 180px; width: 303px; text-align: center; }
  .post-image { width: 303px; height: 204px; }
  .post h3 { margin-top: 30px; font-size: 14.5px; font-weight: 500; color: var(--ink); }
  .post p { margin-top: 22px; font-size: 13.8px; line-height: 23px; color: var(--muted); }
  .btn-read { display: inline-flex; margin-top: 27px; width: 139px; height: 39px; align-items: center; justify-content: center; background: var(--btn-dark); color: var(--white); font-size: 14px; font-weight: 600; }

  /* Footer */
  .site-footer { height: 83px; background: var(--footer-bg); }
  .copyright { left: 115px; top: 42px; font-size: 11px; font-weight: 600; color: #4b4e52; }
  .footer-nav { left: 568px; top: 39px; display: flex; gap: 21px; font-size: 14px; font-weight: 500; color: var(--ink); }
</style>
</head>
<body>
<svg width="0" height="0" style="position:absolute">
  <defs>
    <symbol id="icon-share" viewBox="0 0 60 52">
      <path d="M36 4 L56 22 L36 40 L36 30 C22 29 12 34 4 47 C6 28 16 16 36 14 Z" fill="none" stroke="#e35d3a" stroke-width="2.6" stroke-linejoin="round"/>
    </symbol>
  </defs>
</svg>

<header class="hero">
  <div class="abs hero-side"></div>
  <div class="abs brand"><span class="brand-dot"></span><span class="brand-name">Brisk Trail</span></div>
  <nav class="abs nav">
    <a class="active">About</a><a>Pricing</a><a>Blog</a><a>FAQs</a><a>Support</a><a>Reviews</a><a>Free-Trail</a><a>Contact</a>
  </nav>
  <div class="abs btn-login">Login</div>
  <div class="abs hero-art" role="img" aria-label="Isometric illustration of a laptop with filing drawers and a businessman holding an orange folder"></div>
  <h1 class="abs hero-title">Find that document<br>or item instantly.</h1>
  <p class="abs hero-text">Brisk-Trail is a system that allows you to quickly search for the location of every item that you store or file. It is an essential tool for keeping track of paper documents or any other kind of physical item. You'll have the ability to quickly find any item you're searching for, even years after you've stored it. More importantly, using Brisk-Trail helps you save considerable space without losing speedy accessibility to your treasured items.</p>
  <p class="abs hero-lead">Keeping track of all your paper documents and other belongings has never been easier!</p>
  <div class="abs btn-contact">Contact</div>
</header>

<section class="why-use">
  <h2 class="abs section-heading">Why use a storage management system like Brisk-Trail?</h2>
  <div class="abs kicker">MANAGING PAPER DOCUMENTS</div>
  <div class="abs why-copy">
    <p>Most people and businesses have a variety of documents that need to be filed. The problem is how to do it efficiently so that anything you need can easily be found, even well into the future. Normally, you'd put them in folders on file drawers, sorted in some sort of fashion. But which standard is correct for all kinds of documents? There is no set criterion for every kind of document, so you need to use a combination of them.</p>
    <p>As time passes, you might have a difficult time recalling what criterion you used to file your documents, making it hard to find that document with ease. You might not even find it at all. It becomes even more complex when the person doing the searching isn't the same one as who filed it years ago.</p>
    <p>It is estimated that workers spend over 20% of their time managing documents. A storage management system like Brisk-Trail allows any authorized user to instantly find any document regardless of who filed it or which criterion was used, as long as it was properly filed using the system.</p>
  </div>
  <div class="abs why-art" role="img" aria-label="Illustration of a smartphone with open drawers and a businessman carrying a large orange binder"></div>
</section>

<section class="objects">
  <h2 class="abs center-title">Managing any non-document objects</h2>
  <p class="abs objects-sub">The same is true of storing any other kind of objects. Common examples include:</p>
  <div class="abs object-item" style="top:207px">
    <svg><use href="#icon-share"/></svg>
    <div><h3>Storage boxes, closets, warehouses, and shelves</h3>
    <p>Anything that you put away in storage, would better be indexed with a system that lets you find what you're looking for instantly. Otherwise, you are better off getting rid of those items. In addition to helping you find any object quickly and easily, proper use of Brisk-Trail could help you save lots of space!</p></div>
  </div>
  <div class="abs object-item" style="top:345px">
    <svg><use href="#icon-share"/></svg>
    <div><h3>Books</h3>
    <p>Whether you keep your books on display on shelves, or stored in boxes, you should keep them indexed if you ever want to find any of them in the future.</p></div>
  </div>
  <div class="abs object-item" style="top:451px">
    <svg><use href="#icon-share"/></svg>
    <div><h3>Wines</h3>
    <p>Maintaining a constant temperature is essential for good care of quality wines. If you are a wine enthusiast, and have even a small wine cellar fridge, keeping your wines indexed on our system would prove invaluable in selecting and locating a wine bottle for any moment without opening that cellar fridge door for too long.</p></div>
  </div>
  <div class="abs object-item" style="top:587px">
    <svg><use href="#icon-share"/></svg>
    <div><h3>Safety boxes</h3>
    <p>It is common for people to forget exactly which valuables they have stored in their safety boxes or bank safety deposit boxes.</p></div>
  </div>
  <div class="abs down-btn">
    <svg width="24" height="24" viewBox="0 0 24 24"><path d="M12 4 V19 M5 12 L12 19 L19 12" fill="none" stroke="#fff" stroke-width="2.4" stroke-linecap="round" stroke-linejoin="round"/></svg>
  </div>
</section>

<section class="reasons">
  <h2 class="abs center-title">Why Brisk-Trail?</h2>
  <div class="abs reason" style="top:164px"><svg><use href="#icon-share"/></svg><span>It is extremely easy to use.</span></div>
  <div class="abs reason" style="top:219px"><svg><use href="#icon-share"/></svg><span>It Adapts to your stile. Since each catalog can have 1 or more levels of depth (folders and sub-folders), Brisk-Trail does not force you to use a specific filing or storage methodology.</span></div>
  <div class="abs reason" style="top:324px"><svg><use href="#icon-share"/></svg><span>It's very affordable. Checkout our pricing plans!</span></div>
  <div class="abs reason" style="top:379px"><svg><use href="#icon-share"/></svg><span>Since it is online, your data is available almost anywhere in the world.</span></div>
  <div class="abs reason" style="top:434px"><svg><use href="#icon-share"/></svg><span>Data encryption ensures that your information is always private, safe, and secure.</span></div>
</section>

<section class="testimonials">
  <h2 class="abs t-title">Testimonials</h2>
  <p class="abs t-sub">Happy Customers</p>
  <svg class="abs t-arrow" style="left:205px" viewBox="0 0 58 26"><path d="M56 13 H3 M13 3 L3 13 L13 23" fill="none" stroke="#bfc1c3" stroke-width="2.2"/></svg>
  <blockquote class="abs t-quote">Outstanding work from Lorem Text. They delivered<br>on time and helped me through this whole<br>process.&nbsp; I am definitely going to work again with<br>them - 10/10 Stars in all aspects.</blockquote>
  <svg class="abs t-arrow" style="left:1036px" viewBox="0 0 58 26"><path d="M2 13 H55 M45 3 L55 13 L45 23" fill="none" stroke="#bfc1c3" stroke-width="2.2"/></svg>
  <p class="abs t-name">On Time Delivery</p>
  <p class="abs t-company">Halvern GmbH Learning Systems Company</p>
  <p class="abs t-role">Founder</p>
</section>

<section class="blog">
  <h2 class="abs center-title">Blog</h2>
  <div class="abs blog-rule"></div>
  <article class="abs post" style="left:124px">
    <div class="post-image" role="img" aria-label="Photo of a smiling woman holding a tablet against a yellow background" style="background:linear-gradient(135deg,#f7b500,#f2c418)"></div>
    <h3>Lorem Ipsum Dolor</h3>
    <p>Lorem ipsum dolor sit amet, consectetur adipiscing elit, sed do eiusmod tempor incididunt ut labore et dolore magna aliqua.</p>
    <span class="btn-read">Read More</span>
  </article>
  <article class="abs post" style="left:448px">
    <div class="post-image" role="img" aria-label="Photo of two dogs against a pink background" style="background:linear-gradient(135deg,#f6b4c4,#f3a9bb)"></div>
    <h3>Lorem Ipsum Dolor</h3>
    <p>Lorem ipsum dolor sit amet, consectetur adipiscing elit, sed do eiusmod tempor incididunt ut labore et dolore magna aliqua.</p>
    <span class="btn-read">Read More</span>
  </article>
  <article class="abs post" style="left:771px">
    <div class="post-image" role="img" aria-label="Photo of a child in a face mask giving a thumbs up on a grey background" style="background:linear-gradient(135deg,#e4e4e2,#c9a04a)"></div>
    <h3>Lorem Ipsum Dolor</h3>
    <p>Lorem ipsum dolor sit amet, consectetur adipiscing elit, sed do eiusmod tempor incididunt ut labore et dolore magna aliqua.</p>
    <span class="btn-read">Read More</span>
  </article>
</section>

<footer class="site-footer">
  <p class="abs copyright">© 2021 Brisk-Trail.&nbsp; All Rights Reserved.</p>
  <nav class="abs footer-nav"><span>About</span><span>Pricing</span><span>Blog</span><span>FAQs</span><span>Support</span><span>Reviews</span><span>Free-Trail</span><span>Contact</span></nav>
</footer>
</body>
</html>
```